Introduction flyer

Bright Harvest Nutrition & Wellness Consulting, is a new holistic nutritional therapy specialising in womens health. I want a flyer that appeals to women between 15 to 60. It must speak "health, food & balance". I have attached the basic info I need included in the text. I like Greens & Blues, soft text. My flyer will be distributed to cafes, shops, fitness centres, hung up in grocery stores & health centres etc. The QERV & DLUP logos need to appear on the flyer to show I am fully registered. My own logo & company name is attached.

Target Market(s)

Women from 10 to 60 years old.

Industry/Entity Type

Nutritionist

Colors
32a6d7
abd037
33b8a4
fbf289
ffcf3e
b768aa
d5d5d5
dcdcdc
e8e8e8

Requirements
Must have
• An image of healthy food & ladies. A group of women eating soup, stews or curry type dishes, with plenty of colour - no bread or white wine, and not just fruit please. Food that looks enjoyable to the average person.
• Nutrition is main part of my job, so please keep that in mind & emphasise food & natural well being.
Should not have
• People exercising, men, white wine, bread, cakes, sweets etc..

```html
<!DOCTYPE html>
<html lang="en">
<head>
<meta charset="utf-8">
<title>Bright Harvest Nutrition – Introduction Flyer</title>
<link href="https://fonts.googleapis.com/css2?family=Open+Sans:wght@400;600;700;800&family=Oswald:wght@500;600&family=Cinzel:wght@400&display=swap" rel="stylesheet">
<style>
  :root {
    --page-bg: #e6e2dc;
    --white: #ffffff;
    --ink: #3b3b3b;
    --blue: #2f63a8;
    --blue-band: #3a72b5;
    --green: #1f8a3a;
    --green-panel: #17883a;
    --teal-band: #2aa2be;
    --grey-panel: #e9ecec;
    --dark-panel: #262d2a;
    --tick: #2a9a48;
    --purple: #6b3b97;
  }
  * { box-sizing: border-box; margin: 0; padding: 0; }
  html, body { width: 1028px; height: 1200px; overflow: hidden; }
  body {
    background: var(--page-bg);
    font-family: "Open Sans", Arial, sans-serif;
    color: var(--ink);
    position: relative;
  }
  .flyer {
    position: absolute;
    left: 109px; top: 27px;
    width: 810px; height: 1145px;
    background: var(--white);
    overflow: hidden;
    box-shadow: 0 2px 10px rgba(0,0,0,.18);
  }
  .photo { position: absolute; }
  .photo--fruit-basket { left: 0; top: 0; width: 505px; height: 398px;
    background: linear-gradient(180deg, #0d0b09 0%, #3a2410 38%, #9c2a1c 55%, #a9b847 70%, #d8b38a 85%, #c79a6e 100%); }
  .photo--women-dining { left: 516px; top: 0; width: 294px; height: 250px;
    background: linear-gradient(160deg, #b99770 0%, #8a6a48 45%, #e9e1d6 70%, #6e5236 100%); }
  .photo--berry-glass { left: 516px; top: 261px; width: 141px; height: 137px;
    background: linear-gradient(180deg, #f1f0ee 0%, #e4e2e0 60%, #d7d3d2 100%); }
  .photo--vegetables { left: 668px; top: 261px; width: 142px; height: 137px;
    background: linear-gradient(135deg, #f5f3ef 0%, #4d8a2e 40%, #e0642a 65%, #c2302b 85%, #f4f2ee 100%); }

  .brand {
    position: absolute; left: 20px; top: 84px; width: 224px;
    text-align: center; color: var(--white);
  }
  .brand__mark { display: block; width: 10px; height: 10px; border-radius: 50%; background: var(--white); margin: 0 auto 8px; }
  .brand__name { font-family: "Open Sans", sans-serif; font-size: 11px; font-weight: 400; letter-spacing: .4px; line-height: 1.3; }

  .headline { position: absolute; left: 41px; top: 415px; text-transform: uppercase; }
  .headline__line { display: block; white-space: nowrap; }
  .headline__line--1 { font-size: 38px; color: var(--blue); line-height: 48px; }
  .headline__line--2 { font-size: 24px; color: var(--green); line-height: 34px; }
  .headline__line--3 { font-size: 30px; color: var(--green); line-height: 40px; }
  .headline strong { font-weight: 800; }
  .headline .is-green { color: var(--green); }
  .headline .is-blue { color: var(--blue); }

  .visit-band {
    position: absolute; left: 0; top: 550px; width: 810px; height: 68px;
    background: var(--blue-band); color: var(--white);
    font-weight: 700; font-size: 19px; line-height: 28px; padding: 6px 40px;
  }

  .intro {
    position: absolute; left: 0; top: 618px; width: 522px; height: 206px;
    background: var(--grey-panel); padding: 8px 20px 0 42px;
  }
  .intro__title { font-size: 19.5px; font-weight: 700; color: var(--green); line-height: 28px; text-transform: uppercase; }
  .intro__sub { font-size: 19.5px; font-weight: 700; color: var(--blue); line-height: 22px; text-transform: uppercase; margin-bottom: 10px; }
  .intro__body { font-size: 13.5px; line-height: 18.6px; color: #444; }

  .specialism-band {
    position: absolute; left: 0; top: 828px; width: 522px; height: 25px;
    background: var(--teal-band); color: var(--white);
    font-size: 15px; font-weight: 700; line-height: 25px; padding-left: 44px;
  }
  .specialisms { position: absolute; left: 44px; top: 866px; width: 470px; list-style: none; }
  .specialisms li { position: relative; padding-left: 35px; font-size: 13.8px; line-height: 16.5px; margin-bottom: 10.7px; color: #444; }
  .specialisms li svg { position: absolute; left: 0; top: 3px; }

  .contact { position: absolute; left: 522px; top: 618px; width: 288px; height: 527px; background: var(--green-panel); }
  .contact__call { height: 87px; background: var(--dark-panel); color: var(--white); text-align: center; font-family: "Oswald", sans-serif; padding-top: 8px; }
  .contact__call-label { font-size: 23px; font-weight: 500; letter-spacing: .3px; line-height: 30px; }
  .contact__phone { font-size: 41px; font-weight: 600; line-height: 46px; letter-spacing: .5px; }
  .contact__email { height: 30px; background: var(--blue-band); color: var(--white); text-align: center; font-size: 14px; font-weight: 700; line-height: 30px; }
  .contact__offer { padding: 12px 16px 0 20px; color: var(--white); }
  .contact__lead { font-size: 17px; line-height: 22px; }
  .contact__free { font-size: 29px; line-height: 34px; }
  .contact__big { font-size: 32px; font-weight: 800; line-height: 36px; }
  .contact__note { font-size: 12.5px; line-height: 17px; margin-top: 8px; }
  .contact__note + .contact__note { margin-top: 12px; }

  .registrations {
    position: absolute; left: 0; top: 399px; width: 288px; height: 81px; background: var(--white);
    display: flex; align-items: center; justify-content: space-around; padding: 0 14px;
  }
  .reg { display: flex; align-items: center; gap: 6px; font-size: 30px; font-weight: 700; }
  .reg__dot { width: 22px; height: 22px; border-radius: 50%; }
  .reg--dlup { color: var(--green); }
  .reg--dlup .reg__dot { background: var(--blue); }
  .reg--qerv { color: var(--purple); }
  .reg--qerv .reg__dot { background: var(--purple); }
</style>
</head>
<body>
  <main class="flyer">
    <div class="photo photo--fruit-basket" role="img" aria-label="Basket of fresh fruit: apples, pears, oranges, strawberries and green grapes on a dark background"></div>
    <div class="photo photo--women-dining" role="img" aria-label="Group of women sharing colourful vegetable dishes around a wooden table"></div>
    <div class="photo photo--berry-glass" role="img" aria-label="Glass of yoghurt with falling berries"></div>
    <div class="photo photo--vegetables" role="img" aria-label="Fresh vegetables, carrots, broccoli, tomatoes and strawberries"></div>

    <div class="brand">
      <span class="brand__mark"></span>
      <p class="brand__name">BRIGHT HARVEST NUTRITION<br>&amp; Wellness Consulting</p>
    </div>

    <h1 class="headline">
      <span class="headline__line headline__line--1">Do you <strong class="is-green">experience low energy,</strong></span>
      <span class="headline__line headline__line--2">Low libido, <strong class="is-blue">menstrual cycle complications</strong><span class="is-blue">,</span></span>
      <span class="headline__line headline__line--3">or are you planning <strong>a baby?</strong></span>
    </h1>

    <p class="visit-band">Home visits available, at no extra cost within local area; I can visit your place of work or home.</p>

    <section class="intro">
      <h2 class="intro__title">Small changes to your diet may lead to big changes in your health.</h2>
      <p class="intro__sub">Eat well, live well.</p>
      <p class="intro__body">&nbsp;Discover exactly what YOU need to change and how to make these changes long lasting.<br>There is no one-rule-fits-all. My nutritional advice aims to dig up the root cause to my client's health concerns. My lifestyle plans are completely personalised to an individual's needs and circumstances. I consider the whole person not just symptoms or disease.</p>
    </section>

    <h3 class="specialism-band">THERAPIST &amp; WELLNESS CONSULTANT, SPECIALISING IN:</h3>
    <ul class="specialisms">
      <li><svg width="11" height="11" viewBox="0 0 11 11"><rect x=".5" y=".5" width="10" height="10" fill="none" stroke="var(--tick)"/><path d="M2.5 5.5l2 2 4-4.5" fill="none" stroke="var(--tick)" stroke-width="1.6"/></svg>Fertility, IVF, pre-conception, pregnancy &amp; post-natal care</li>
      <li><svg width="11" height="11" viewBox="0 0 11 11"><rect x=".5" y=".5" width="10" height="10" fill="none" stroke="var(--tick)"/><path d="M2.5 5.5l2 2 4-4.5" fill="none" stroke="var(--tick)" stroke-width="1.6"/></svg>Menstrual cycle challenges (PCOS, Endometriosis, PMS, heavy/irregular periods etc)</li>
      <li><svg width="11" height="11" viewBox="0 0 11 11"><rect x=".5" y=".5" width="10" height="10" fill="none" stroke="var(--tick)"/><path d="M2.5 5.5l2 2 4-4.5" fill="none" stroke="var(--tick)" stroke-width="1.6"/></svg>Thyroid conditions</li>
      <li><svg width="11" height="11" viewBox="0 0 11 11"><rect x=".5" y=".5" width="10" height="10" fill="none" stroke="var(--tick)"/><path d="M2.5 5.5l2 2 4-4.5" fill="none" stroke="var(--tick)" stroke-width="1.6"/></svg>Low libido</li>
      <li><svg width="11" height="11" viewBox="0 0 11 11"><rect x=".5" y=".5" width="10" height="10" fill="none" stroke="var(--tick)"/><path d="M2.5 5.5l2 2 4-4.5" fill="none" stroke="var(--tick)" stroke-width="1.6"/></svg>Digestive health</li>
      <li><svg width="11" height="11" viewBox="0 0 11 11"><rect x=".5" y=".5" width="10" height="10" fill="none" stroke="var(--tick)"/><path d="M2.5 5.5l2 2 4-4.5" fill="none" stroke="var(--tick)" stroke-width="1.6"/></svg>Chronic fatigue syndrome</li>
      <li><svg width="11" height="11" viewBox="0 0 11 11"><rect x=".5" y=".5" width="10" height="10" fill="none" stroke="var(--tick)"/><path d="M2.5 5.5l2 2 4-4.5" fill="none" stroke="var(--tick)" stroke-width="1.6"/></svg>Perimenopause/menopause</li>
      <li><svg width="11" height="11" viewBox="0 0 11 11"><rect x=".5" y=".5" width="10" height="10" fill="none" stroke="var(--tick)"/><path d="M2.5 5.5l2 2 4-4.5" fill="none" stroke="var(--tick)" stroke-width="1.6"/></svg>Weight management</li>
      <li><svg width="11" height="11" viewBox="0 0 11 11"><rect x=".5" y=".5" width="10" height="10" fill="none" stroke="var(--tick)"/><path d="M2.5 5.5l2 2 4-4.5" fill="none" stroke="var(--tick)" stroke-width="1.6"/></svg>Type 2 diabetes, blood sugar dysregulation, high blood pressure, high cholesterol</li>
    </ul>

    <aside class="contact">
      <div class="contact__call">
        <p class="contact__call-label">CALL MAEVE TODAY ON</p>
        <p class="contact__phone">085-2736-418</p>
      </div>
      <p class="contact__email">maeve@brightharvestnutrition.ie</p>
      <div class="contact__offer">
        <p class="contact__lead"><strong>To book a</strong> consultation or for a</p>
        <p class="contact__free"><strong>free</strong> no obligation</p>
        <p class="contact__big">15-minute mini consultation.</p>
        <p class="contact__note">Initial consultations typically last up to 2 hours, follow-ups 30 – 60 minutes.</p>
        <p class="contact__note">An in-depth case history is gathered during the initial consultation. This includes all aspects of your lifestyle both past and present, from what you eat to how you sleep.</p>
      </div>
      <div class="registrations">
        <span class="reg reg--dlup"><span class="reg__dot"></span>DLUP</span>
        <span class="reg reg--qerv"><span class="reg__dot"></span>QERV</span>
      </div>
    </aside>
  </main>
</body>
</html>
```